Background of Our Business: TQB Financial Services provides accounting and tax services to small businesses. Website: www.tqbfsx.com.au. Our slogan is: one stop finance department service for small businesses.
I would like a flyer design with 2 sides.
1st side)
Business Logo; TQB - Finance Department Service for Small Businesses (Please refer file 1 as attached)

Large text of: Too many things going on? Smaller text: Let us reduce your input into accounts, you can focus on more value adding areas.

Our Services: Bookkeeping, Payroll, Financial Statement, Tax Advisory, Tax Return, Business Performance Measurement, Business Decision Support, Assistance in Loan Applications, and much more.

Why Us: Our clients are handpicked, we are fully committed to your business, and our works are performed at corporate standard. We utilise technology to save your accounting cost, monitor your compliance risks, provide solid data for business decision making, and be your representative in dealing with banks and NRB. (Please also refer file 2 as attached)

Contact details: Address: 58 Dunmore Street, Carlisle, WA 6101
PO Box 2493, East Victoria Park, WA 6981
Tel: (08) 6287 3914; Mob: 0491 738 226

2nd side)
Our Pricing: Charge by transaction volumes; Fixed fee advised beforehand. hourly rate please refer file 4 as attached.

Our 'Gold' level service subscriber receives:
Frequent bookkeeping, payroll, and financial reporting services
Integrate tax advisory, compliance risk monitoring and control
Free regular preliminary business performance check
Free assistance in commercial loan and mortgage application
Free hand picked business insights for your industry
Free representative service for you in dealing with banks, NRB.

Coupon Section: Sign up now and receive 10% off for your next 12 months bill. Valid until 31/07/2016.

```html
<!DOCTYPE html>
<html lang="en">
<head>
<meta charset="utf-8">
<title>TQB Financial Services – Flyer</title>
<link href="https://fonts.googleapis.com/css2?family=Anton&family=Cinzel:wght@700&family=PT+Sans:ital,wght@0,400;0,700;1,700&family=Questrial&display=swap" rel="stylesheet">
<style>
:root{
  --navy:#0b3a6d;
  --navy-deep:#093563;
  --sky:#17b4ef;
  --sky-card:#0fbdf6;
  --sky-text:#1aa6e4;
  --white:#ffffff;
  --paper-grey:#e5e5e5;
  --backdrop:#2b2b2b;
  --ink:#1b1b1b;
}
*{margin:0;padding:0;box-sizing:border-box}
html,body{width:1200px;height:1051px;overflow:hidden;background:var(--backdrop)}
.stage{position:relative;width:1200px;height:1051px}
.flyer{position:absolute;width:549px;height:775px;overflow:hidden}
.flyer--front{left:53px;top:81px;background:var(--white)}
.flyer--back{left:623px;top:78px;background:var(--navy)}

/* front */
.front-body{position:absolute;left:42px;top:0;right:30px}
.brand{position:absolute;top:48px;left:0;display:flex;align-items:center;gap:12px}
.brand__mark{width:20px;height:20px;background:var(--navy)}
.brand__name{font-family:"Questrial",sans-serif;font-weight:400;font-size:54px;line-height:56px;color:var(--navy);letter-spacing:3px}
.brand__rule{position:absolute;top:112px;left:0;width:243px;height:1px;background:#9aa9bb}
.brand__tagline{position:absolute;top:116px;left:0;font-family:"Questrial",sans-serif;font-size:10.5px;color:var(--navy);white-space:nowrap}
.headline{position:absolute;top:148px;left:0;font-family:"Cinzel",serif;font-weight:700;font-size:45px;line-height:44px;color:var(--navy);letter-spacing:1px;white-space:nowrap}
.subhead{position:absolute;top:240px;left:0;width:455px;font-family:"PT Sans",sans-serif;font-style:italic;font-weight:700;font-size:21.5px;line-height:28px;color:var(--sky-text)}
.tab{position:absolute;left:0;height:22px;width:126px;background:var(--navy);color:var(--white);font-family:"Questrial",sans-serif;font-weight:400;font-size:13.5px;line-height:22px;padding-left:6px;border-radius:0 11px 11px 0}
.copy{position:absolute;left:0;width:478px;font-family:"Questrial",sans-serif;font-size:14.4px;line-height:16px;color:var(--ink)}
.web{position:absolute;left:0;font-family:"Questrial",sans-serif;font-size:13px;letter-spacing:3.2px;color:var(--navy)}

/* coupon */
.coupon{position:absolute;left:0;width:549px;height:112px}
.coupon--front{top:663px;background:var(--navy);color:var(--white)}
.coupon--back{top:663px;background:var(--paper-grey);color:var(--navy)}
.coupon__cut{position:absolute;top:2px;left:0;width:100%;height:0;border-top:1.5px dashed currentColor;opacity:.8}
.coupon__scissors{position:absolute;top:-4px;right:14px;width:22px;height:12px}
.coupon__lead{position:absolute;top:34px;left:118px;width:100px;text-align:right;font-family:"Questrial",sans-serif;font-size:14px;line-height:16px}
.coupon__big{position:absolute;top:16px;left:222px;font-family:"Anton",sans-serif;line-height:1;white-space:nowrap}
.coupon__num{font-size:52px;letter-spacing:-1px}
.coupon__off{font-size:33px;letter-spacing:-.5px}
.coupon__tail{position:absolute;top:30px;left:364px;font-family:"Questrial",sans-serif;font-size:14px;line-height:16px}
.coupon__valid{position:absolute;top:75px;left:207px;width:162px;height:21px;border-radius:11px;background:var(--sky);color:var(--navy);font-family:"Questrial",sans-serif;font-size:13px;line-height:21px;text-align:center}

/* back */
.tiers{position:absolute;top:50px;left:30px;display:flex;gap:6px}
.tier{width:158px;height:368px;background:var(--sky-card);border-radius:6px;padding:0 5px;color:var(--ink)}
.tier__name{height:42px;display:flex;align-items:center;justify-content:center;text-align:center;font-family:"PT Sans",sans-serif;font-weight:700;font-size:19px;line-height:16px;color:var(--navy-deep)}
.tier__rates{border:1px dashed var(--navy);padding:6px 6px;font-family:"PT Sans",sans-serif;font-size:8.4px;line-height:12px}
.tier__notes{padding:10px 2px 0 5px;font-family:"PT Sans",sans-serif;font-size:8.4px;line-height:12px}
.tier__notes p{margin-bottom:12px}
.perks-title{position:absolute;top:465px;left:42px;font-family:"PT Sans",sans-serif;font-weight:700;font-size:14px;color:var(--sky)}
.perks{position:absolute;top:487px;left:42px;list-style:none;font-family:"Questrial",sans-serif;font-size:14.5px;line-height:20px;color:var(--white)}
.perks li::before{content:"•";color:var(--sky);display:inline-block;width:13px}
.flyer--back .web{left:42px;top:619px;color:var(--sky)}
</style>
</head>
<body>
<main class="stage">

  <section class="flyer flyer--front">
    <div class="front-body">
      <div class="brand"><span class="brand__mark"></span><span class="brand__name">TQB</span></div>
      <div class="brand__rule"></div>
      <p class="brand__tagline">Finance Department Service for Small Businesses</p>
      <h1 class="headline">Too many things<br>going on?</h1>
      <p class="subhead">Let us reduce your input into accounts, you can focus on more value adding areas.</p>

      <h2 class="tab" style="top:316px">Ourservices</h2>
      <p class="copy" style="top:348px">Bookkeeping, Payroll, Financial Statement, Tax Advisory, Tax Return, Business Performance Measurement, Business Decision Support, Assistance in Loan Applications, and much more.</p>

      <h2 class="tab" style="top:406px">Why Us</h2>
      <p class="copy" style="top:438px">Our clients are handpicked, we are fully committed to your business, and our works are performed at corporate standard. We utilise technology to save your accounting cost, monitor your compliance risks, provide solid data for business decision making, and be your representative in dealing with banks and NRB.</p>

      <h2 class="tab" style="top:527px">Contact address</h2>
      <p class="copy" style="top:562px">58 Dunmore Street, Carlisle, WA 6101<br>PO Box 2493, East Victoria Park, WA 6981<br>Tel: (08) 6287 3914; Mob: 0491 738 226</p>
      <p class="web" style="top:619px">www.tqbfsx.com.au.</p>
    </div>

    <div class="coupon coupon--front">
      <div class="coupon__cut"></div>
      <svg class="coupon__scissors" viewBox="0 0 22 12" fill="none" stroke="currentColor" stroke-width="1.2"><circle cx="18" cy="3" r="2.3"/><circle cx="18" cy="9" r="2.3"/><path d="M16 4 L2 9 M16 8 L2 3"/></svg>
      <p class="coupon__lead">Sign up now &amp;<br>receive</p>
      <p class="coupon__big"><span class="coupon__num">10</span><span class="coupon__off">% off</span></p>
      <p class="coupon__tail">for your next<br>12 months bill.</p>
      <p class="coupon__valid">Valid until 31/07/2016.</p>
    </div>
  </section>

  <section class="flyer flyer--back">
    <div class="tiers">
      <article class="tier">
        <h3 class="tier__name">Bronze</h3>
        <div class="tier__rates">Bookkeeping &amp; Payroll : $50/hr<br>Taxation : $110/hr<br>Management Accounting : $110/hr<br>Finance : POA, Generally Free<br>General Consulting : Free*</div>
        <div class="tier__notes">
          <p>Rate above applies for using us for bookkeeping or payroll or taxation or management accounting service only.</p>
          <p>Other fees/charges may apply for client subscriptions, e.g. accounting software subscription, currently around $50/month.</p>
          <p>All hours and fees will be agreed upfront, no surprises.</p>
          <p>*Free charge for consulting in general topics, without us have to go through large quantities of documents. Fees will be advised beforehand if there is any.</p>
        </div>
      </article>
      <article class="tier">
        <h3 class="tier__name">Gold<br>(Most Popular)</h3>
        <div class="tier__rates">Bookkeeping &amp; Payroll : $45/hr<br>Taxation : $99/hr<br>Management Accounting : $99/hr<br>Finance : POA, Generally Free<br>General Consulting : Free*</div>
        <div class="tier__notes">
          <p>Rate above applies for using us for bookkeeping or payroll or management accounting and taxation services.</p>
          <p>Other fees/charges may apply for client subscriptions, e.g. accounting software subscription, currently around $50/month.</p>
          <p>All hours and fees will be agreed upfront, no surprises.</p>
          <p>*Free charge for consulting in general topics, which without us have to go through large quantities of documents. Fees will be advised beforehand if there is any.</p>
        </div>
      </article>
      <article class="tier">
        <h3 class="tier__name">Plantium</h3>
        <div class="tier__rates">Bookkeeping &amp; Payroll : $40/hr<br>Taxation : $88/hr<br>Management Accounting : $88/hr<br>Finance : POA, Generally Free<br>General Consulting : Free*</div>
        <div class="tier__notes">
          <p>Rate above applies for using us for bookkeeping or payroll or management accounting and taxation services.</p>
          <p>Other fees/charges may apply for client subscriptions, e.g. accounting software subscription, currently around $50/month.</p>
          <p>All hours and fees will be agreed upfront, no surprises.</p>
          <p>*Free charge for consulting in general topics, which without us have to go through large quantities of documents. Fees will be advised beforehand if there is any.</p>
        </div>
      </article>
    </div>

    <h2 class="perks-title">Our 'Gold' level service subscriber receives:</h2>
    <ul class="perks">
      <li>Frequent bookkeeping, payroll, and financial reporting services</li>
      <li>Integrate tax advisory, compliance risk monitoring and control</li>
      <li>Free regular preliminary business performance check</li>
      <li>Free assistance in commercial loan and mortgage application</li>
      <li>Free hand picked business insights for your industry</li>
      <li>Free representative service for you in dealing with banks, NRB.</li>
    </ul>
    <p class="web">www.tqbfsx.com.au.</p>

    <div class="coupon coupon--back">
      <div class="coupon__cut"></div>
      <svg class="coupon__scissors" viewBox="0 0 22 12" fill="none" stroke="currentColor" stroke-width="1.2"><circle cx="18" cy="3" r="2.3"/><circle cx="18" cy="9" r="2.3"/><path d="M16 4 L2 9 M16 8 L2 3"/></svg>
      <p class="coupon__lead">Sign up now &amp;<br>receive</p>
      <p class="coupon__big"><span class="coupon__num">10</span><span class="coupon__off">% off</span></p>
      <p class="coupon__tail">for your next<br>12 months bill.</p>
      <p class="coupon__valid">Valid until 31/07/2016.</p>
    </div>
  </section>

</main>
</body>
</html>
```